Business card design needed

It's a new business in town.Something so the name stands out.I need a logo for the B.R.W
I may all so use the design as a sign on a building

Contact Information for Business Card

B.R.W
Brindlewood Auto Detailing
42 Fenwarra Crs
Brindlewood Vic 3799
Ph:(03)59284736
Mob:0417362958

```html
<!DOCTYPE html>
<html lang="en">
<head>
<meta charset="utf-8">
<title>Brindlewood Auto Detailing – Business Card</title>
<link rel="stylesheet" href="https://fonts.googleapis.com/css2?family=Michroma&display=swap">
<style>
  :root {
    --backdrop: #2b2b2b;
    --card-white: #f4f4f4;
    --ink-dark: #2a2a2a;
    --brand-blue: #1b8db4;
    --label-blue: #1fa3d6;
    --teal-glow: #0ea9dc;
    --teal-mid: #0a7898;
    --teal-edge: #073d4c;
    --white: #ffffff;
  }
  * { box-sizing: border-box; margin: 0; padding: 0; }
  html, body {
    width: 1200px;
    height: 900px;
    overflow: hidden;
    background: var(--backdrop);
    font-family: "Michroma", sans-serif;
  }
  .canvas {
    position: relative;
    width: 1200px;
    height: 900px;
  }
  .card {
    position: absolute;
    width: 560px;
    height: 320px;
    box-shadow: 0 18px 40px rgba(0,0,0,0.55);
    text-transform: uppercase;
  }
  /* Front: white contact card */
  .card--front {
    left: 130px;
    top: 110px;
    background: var(--card-white);
  }
  .front-brand {
    position: absolute;
    left: 36px;
    bottom: 40px;
  }
  .front-brand__name {
    font-size: 50px;
    line-height: 1;
    color: var(--brand-blue);
    letter-spacing: 2px;
  }
  .front-brand__tagline {
    margin-top: 8px;
    font-size: 11px;
    color: var(--ink-dark);
    letter-spacing: 0.5px;
  }
  .contact {
    position: absolute;
    left: 300px;
    top: 118px;
    font-size: 10.5px;
    line-height: 1.55;
    color: var(--ink-dark);
  }
  .contact__label { color: var(--label-blue); }
  /* Back: teal logo card */
  .card--back {
    left: 510px;
    top: 470px;
    background: radial-gradient(ellipse at 55% 45%, var(--teal-glow) 0%, var(--teal-mid) 45%, var(--teal-edge) 100%);
    display: flex;
    flex-direction: column;
    align-items: center;
    justify-content: center;
  }
  .back-brand__name {
    font-size: 88px;
    line-height: 1;
    color: var(--white);
    letter-spacing: 4px;
  }
  .back-brand__tagline {
    margin-top: 12px;
    font-size: 19px;
    color: var(--white);
    letter-spacing: 0.5px;
  }
</style>
</head>
<body>
<main class="canvas">
  <section class="card card--front" aria-label="Business card front">
    <div class="front-brand">
      <div class="front-brand__name">B.R.W</div>
      <div class="front-brand__tagline">Brindlewood Auto Detailing</div>
    </div>
    <address class="contact" style="font-style: normal;">
      <div>42 Fenwarra Crs Brindlewood</div>
      <div>Vic 3799</div>
      <div><span class="contact__label">Ph:</span> (03)59284736 <span class="contact__label">Mob:</span> 0417362958</div>
    </address>
  </section>

  <section class="card card--back" aria-label="Business card back">
    <div class="back-brand__name">B.R.W</div>
    <div class="back-brand__tagline">Brindlewood Auto Detailing</div>
  </section>
</main>
</body>
</html>
```